Bcard and stationary
Business card and stationary - Health
Business card and stationary
Bright & Fun-filled
Martin Falkner
Managing Director
418 Birch Lane #d305 Plymouth, MA 02371
martin@ploverstonewellness.com
ploverstonewellness.com

```html
<!DOCTYPE html>
<html lang="en">
<head>
<meta charset="utf-8">
<title>Ploverstone Wellness Stationery</title>
<link rel="stylesheet" href="https://fonts.googleapis.com/css2?family=Lato:wght@400;700&display=swap">
<style>
:root{
  --bg:#ececec;
  --paper:#ffffff;
  --navy:#163a74;
  --blue:#1d5fb3;
  --sky:#3ca9ea;
  --ink:#4a4a4a;
  --cell:#cfd2d6;
  --rule:#9aa0a6;
}
*{box-sizing:border-box;margin:0;padding:0}
html,body{width:1200px;height:552px;overflow:hidden;background:var(--bg);font-family:"Lato",sans-serif;color:var(--ink)}
.stage{position:relative;width:1200px;height:552px}
.sheet{position:absolute;background:var(--paper);box-shadow:0 1px 4px rgba(0,0,0,.18)}
.letter{top:19px;width:348px;height:514px}
.letter--fax{left:12px}
.letter--plain{left:403px}
.brand{position:absolute;display:flex;align-items:center;gap:4px}
.brand__mark{width:12px;height:12px;background:var(--blue)}
.brand__name{font-weight:700;color:var(--navy);text-transform:uppercase;letter-spacing:.6px;font-size:9px;white-space:nowrap}
.letter .brand{left:30px;top:36px}
.contact{position:absolute;font-size:5px;line-height:8px;color:var(--ink)}
.contact li{list-style:none;display:flex;align-items:center;gap:3px}
.contact li::before{content:"";width:4px;height:4px;border-radius:50%;background:var(--blue)}
.letter .contact{left:272px;top:22px}
.footer-band{position:absolute;left:0;right:0;bottom:0;height:20px;
  background:linear-gradient(to bottom,#fff 0,#dff1fb 35%,var(--sky) 70%,var(--navy) 100%)}
.fax-title{position:absolute;right:16px;top:86px;font-size:8px;font-weight:700;color:var(--navy)}
.fax-table{position:absolute;left:28px;top:96px;width:302px;border-collapse:collapse;font-size:5px}
.fax-table td{border:1px solid var(--rule);height:15px;padding:0 3px}
.fax-table .label{background:var(--cell);width:32px}
.checks{position:absolute;left:28px;top:167px;display:flex;gap:16px;font-size:5px}
.checks span{display:flex;align-items:center;gap:3px}
.checks span::before{content:"";width:6px;height:6px;border:1px solid var(--rule)}
.card{top:29px;width:139px;height:81px}
.card--front{left:775px}
.card--front .brand{left:10px;top:9px}
.card--front .brand__name{font-size:6px}
.card--front .brand__mark{width:8px;height:8px}
.person{position:absolute;left:22px;top:26px;font-size:5px;line-height:7px}
.person b{color:var(--navy)}
.card--front .contact{left:22px;top:44px;font-size:4px;line-height:6px}
.card--front .footer-band{height:10px}
.card--back{left:936px;background:radial-gradient(ellipse at 50% 45%,var(--sky) 0,var(--blue) 45%,var(--navy) 100%);border-radius:3px}
.card--back .brand,.env-back .brand{left:50%;top:50%;transform:translate(-50%,-50%)}
.card--back .brand__name,.env-back .brand__name{color:#fff;font-size:6px}
.card--back .brand__mark,.env-back .brand__mark{width:8px;height:8px;background:#fff}
.envelope{left:775px;top:192px;width:396px;height:168px}
.envelope .brand{left:14px;top:14px}
.envelope .contact{left:14px;top:118px;font-size:4.5px;line-height:7px}
.envelope .contact li::before{display:none}
.envelope .footer-band{height:14px}
.env-back{left:775px;top:384px;width:396px;height:139px;overflow:hidden}
.env-back svg{position:absolute;left:0;top:0}
.env-back .brand{top:40px}
</style>
</head>
<body>
<main class="stage">

  <section class="sheet letter letter--fax">
    <div class="brand"><span class="brand__mark"></span><span class="brand__name">Ploverstone Wellness</span></div>
    <ul class="contact">
      <li>(508) 555-0142</li>
      <li>(508) 555-0143</li>
      <li>martin@ploverstonewellness.com</li>
      <li>ploverstonewellness.com</li>
    </ul>
    <div class="fax-title">FAX</div>
    <table class="fax-table">
      <tr><td class="label">To:</td><td></td><td class="label">From:</td><td></td></tr>
      <tr><td class="label">Fax:</td><td></td><td class="label">Pages:</td><td></td></tr>
      <tr><td class="label">Phone:</td><td></td><td class="label">Date:</td><td></td></tr>
      <tr><td class="label">Re:</td><td></td><td class="label">CC:</td><td></td></tr>
    </table>
    <div class="checks">
      <span>Urgent</span><span>For Review</span><span>Please Comment</span><span>Please Reply</span><span>Please Recycle</span>
    </div>
    <div class="footer-band"></div>
  </section>

  <section class="sheet letter letter--plain">
    <div class="brand"><span class="brand__mark"></span><span class="brand__name">Ploverstone Wellness</span></div>
    <ul class="contact">
      <li>(508) 555-0142</li>
      <li>(508) 555-0143</li>
      <li>martin@ploverstonewellness.com</li>
      <li>ploverstonewellness.com</li>
    </ul>
    <div class="footer-band"></div>
  </section>

  <section class="sheet card card--front">
    <div class="brand"><span class="brand__mark"></span><span class="brand__name">Ploverstone Wellness</span></div>
    <div class="person"><b>Martin Falkner</b><br>Managing Director</div>
    <ul class="contact">
      <li>(508) 555-0142</li>
      <li>martin@ploverstonewellness.com</li>
      <li>ploverstonewellness.com</li>
    </ul>
    <div class="footer-band"></div>
  </section>

  <section class="sheet card card--back">
    <div class="brand"><span class="brand__mark"></span><span class="brand__name">Ploverstone Wellness</span></div>
  </section>

  <section class="sheet envelope">
    <div class="brand"><span class="brand__mark"></span><span class="brand__name">Ploverstone Wellness</span></div>
    <ul class="contact">
      <li>418 Birch Lane #d305</li>
      <li>Plymouth, MA 02371</li>
      <li>(508) 555-0142</li>
      <li>ploverstonewellness.com</li>
    </ul>
    <div class="footer-band"></div>
  </section>

  <section class="sheet env-back">
    <svg width="396" height="139" viewBox="0 0 396 139" aria-hidden="true">
      <defs>
        <linearGradient id="flapBand" x1="0" y1="0" x2="1" y2="0">
          <stop offset="0" stop-color="#163a74"/>
          <stop offset=".5" stop-color="#3ca9ea"/>
          <stop offset="1" stop-color="#163a74"/>
        </linearGradient>
      </defs>
      <rect x="0" y="0" width="396" height="70" fill="url(#flapBand)"/>
      <path d="M0 70 Q198 100 396 70 L396 78 Q198 108 0 78 Z" fill="#1d5fb3" opacity=".5"/>
    </svg>
    <div class="brand"><span class="brand__mark"></span><span class="brand__name">Ploverstone Wellness</span></div>
  </section>

</main>
</body>
</html>
```